Etikett für Rosé Wein
Zielgruppe
Wir sind ein Weingut das Weine im Premiumsegment produziert.
Wir haben vor einen neuen, hochwertigen Roséwein zu launchen. (Ca. 15 Euro Verkaufspreis)
DIe Flaschenform ist dabei an die Premiumweingüter aus der Provence angelehnt. (als Beispiel Silent Meadow als Datei dabei)
Der Wein wird ein Markenwein sein, das bedeutet der Weinname wir in der Vermarktung wichtiger sein als unser Weingutsname. Der Wein wird unter der Bezeichnung LUMARA vermarket werden.
Der Wein wird eine rose- goldende Kapsel erhalten(ähnlich Silent Meadow) - Datei unserer Kapsel anbei.
Folgende Bestandteile müssen am Etikett zu finden sein.
LUMARA
premium organic Rosé
2021(Jahrgang)
Kessel - Logo(nur die Grafik, nicht der Text Weingut Tobias Kessel der unter dem Logo steht)
Eventuell hätten wir noch gerne ein kleines Icon dabei, etwa eine Illustration eines Vogels oder zBsp. eines Blatt als Skelett oder ähnlich. Oder aber/auch das Logo der alpenländischen Erbkellereien könnte als Icon dienen(ebenfalls als Datei dabei)
Aufgabenstellung
Bei diesem Vorderseiten - Flaschenetikett ist uns eine hochwertige, aussagekräftige Etikette wichtig. Das Etikett muss leicht konisch sein, da die Flasche konisch ist. Die Glasfarbe der Flasche ist weiß durchsichtig, sodass die Farbe des Roseweines gut zur Geltung kommt.
Die max. Etikettenhöhe kann 90 mm betragen. Der Winkel der Flasche ist auf der technischen Zeichnun ersichtlich, von unten nach oben verlaufend, sprich im unteren Teil muss das Etikett schmäler sein als im oberen Bereich. Eine technische Zeichnung der Flasche ist als Datei angehängt.
Ebenso 1. Flaschenfoto einer Originalflache des Mitbewerbs(Fiorello), so wird unsere Flaschen ausssehen.

```html
<!DOCTYPE html>
<html lang="de">
<head>
<meta charset="utf-8">
<title>LUMARA – Premium Organic Rosé</title>
<link href="https://fonts.googleapis.com/css2?family=Questrial&display=swap" rel="stylesheet">
<style>
  :root {
    --backdrop: #fbe6d6;
    --paper: #fbfbfa;
    --ink: #3a3a3a;
    --bird: #5a5a5a;
    --coral: #e68a5c;
    --frame-start: #e68a5c;
    --frame-end: #cf7b78;
  }
  * { margin: 0; padding: 0; box-sizing: border-box; }
  html, body {
    width: 1200px;
    height: 1190px;
    overflow: hidden;
    background: var(--backdrop);
  }
  .label {
    position: absolute;
    left: 60px;
    top: 55px;
    width: 1080px;
    height: 1080px;
    background: var(--paper);
    font-family: "Questrial", "Century Gothic", sans-serif;
    color: var(--ink);
  }
  .vintage {
    position: absolute;
    top: 48px;
    width: 100%;
    text-align: center;
    font-size: 30px;
    letter-spacing: 0.35em;
    padding-left: 0.35em;
  }
  .bird-illustration {
    position: absolute;
    left: 330px;
    top: 120px;
    width: 420px;
    height: 340px;
    border-radius: 48% 52% 40% 60% / 55% 50% 50% 45%;
    background: radial-gradient(ellipse at 45% 55%, #6a6a6a 0%, var(--bird) 55%, #8a8a8a 100%);
    opacity: 0.85;
  }
  .brand-frame {
    position: absolute;
    left: 70px;
    top: 500px;
    width: 940px;
    height: 170px;
    border: 3px solid;
    border-image: linear-gradient(90deg, var(--frame-start), var(--frame-end)) 1;
    display: flex;
    align-items: center;
    justify-content: center;
  }
  .brand-name {
    font-size: 128px;
    color: var(--coral);
    letter-spacing: 0.2em;
    padding-left: 0.2em;
    line-height: 1;
  }
  .ornament {
    position: absolute;
    left: 518px;
    width: 44px;
    height: 30px;
    border-radius: 50% 50% 40% 40%;
    background: var(--coral);
    opacity: 0.9;
  }
  .ornament--top { top: 712px; }
  .ornament--bottom { top: 848px; }
  .wine-type {
    position: absolute;
    top: 770px;
    width: 100%;
    text-align: center;
    font-size: 50px;
    letter-spacing: 0.3em;
    padding-left: 0.3em;
  }
  .winery {
    position: absolute;
    top: 945px;
    width: 100%;
    text-align: center;
    font-size: 44px;
    letter-spacing: 0.08em;
    color: var(--ink);
  }
</style>
</head>
<body>
  <main class="label">
    <div class="vintage">2021</div>
    <div class="bird-illustration" role="img" aria-label="Kupferstich-Illustration einer Schwalbe im Flug"></div>
    <div class="brand-frame">
      <h1 class="brand-name">LUMARA</h1>
    </div>
    <div class="ornament ornament--top" role="img" aria-label="Kleines Lilien-Ornament"></div>
    <p class="wine-type">Premium Organic Rosé</p>
    <div class="ornament ornament--bottom" role="img" aria-label="Kleines Lilien-Ornament"></div>
    <p class="winery">KESSEL</p>
  </main>
</body>
</html>
```